tri fold logistics company FLYER and A4 COMPANY FLYER COVER and A4 company flyer

we need to design company tri fold brochure and A4 company flyer cover for us
our company website is www.halvornfreight.com
pls design for us asap

ALSO OUR COMPANY NAME IS HALVORN FREIGHT INC
NOT " HALVORN FREIGHT, INC"

CAN YOU DESIGN THE COMPANY EMAIL SIGNATURE FOR US TOO

Target Market(s)

customer in U.S.

Industry/Entity Type

Freight Forwarding

Requirements
Must have
• company name and logo
• company name; HALVORN FREIGHT INC
Nice to have
• international shipping map,

```html
<!DOCTYPE html>
<html lang="en">
<head>
<meta charset="utf-8">
<title>Halvorn Freight Inc – Flyer</title>
<link href="https://fonts.googleapis.com/css2?family=Oswald:wght@500;700&family=Roboto:wght@400;500;700&family=Libre+Baskerville:wght@700&display=swap" rel="stylesheet">
<style>
  :root{
    --navy:#0d2a4d;
    --navy-deep:#081c36;
    --blue:#1f8fd6;
    --blue-light:#49b4ef;
    --grey-panel:#e9ecef;
    --grey-text:#4a4f55;
    --white:#ffffff;
    --sun:#f2a23a;
    --dusk:#8a5a3a;
  }
  *{margin:0;padding:0;box-sizing:border-box}
  html,body{width:900px;height:1200px;overflow:hidden;background:#fff}
  .flyer{position:relative;width:900px;height:1200px;background:var(--white);font-family:'Roboto',Arial,sans-serif;color:var(--grey-text);overflow:hidden}

  .header{position:absolute;left:0;top:0;width:900px;height:130px}
  .brand{position:absolute;left:46px;top:36px;display:flex;align-items:center;gap:18px}
  .brand-dot{width:58px;height:58px;border-radius:50%;background:var(--navy)}
  .brand-name{font-family:'Libre Baskerville',Georgia,serif;font-weight:700;font-size:29px;color:var(--navy);letter-spacing:.5px}
  .header-accent{position:absolute;right:0;top:0}

  .hero-photo{position:absolute;left:0;top:130px;width:900px;height:390px;
    background:linear-gradient(180deg,#c9d3da 0%,#e9b46a 42%,var(--sun) 58%,var(--dusk) 100%)}
  .hero-overlay{position:absolute;left:0;top:130px}

  .headline{position:absolute;left:0;top:520px;width:900px;height:165px;
    background:linear-gradient(180deg,rgba(31,143,214,.9) 0%,var(--blue) 40%,#1677bb 100%);padding:20px 0 0 46px}
  .headline h1{font-family:'Oswald',Impact,sans-serif;font-weight:700;font-size:80px;line-height:1;color:var(--white);letter-spacing:1px}
  .headline p{font-family:'Oswald',Impact,sans-serif;font-weight:500;font-size:34px;line-height:1.1;color:var(--white);margin-top:8px;letter-spacing:.5px}
  .headline p strong{font-weight:700}

  .services{position:absolute;left:40px;width:470px}
  .services.ocean{top:708px}
  .services.other{top:900px}
  .services-title{background:var(--navy);color:var(--white);padding:8px 20px;font-family:'Oswald',Impact,sans-serif;font-weight:500;font-size:26px;line-height:1.05;clip-path:polygon(0 0,100% 0,94% 100%,0 100%)}
  .services-title span{display:block;color:var(--blue-light)}
  .services-list{background:var(--grey-panel);padding:10px 16px 10px 32px;list-style:disc;font-size:12.5px;line-height:18px;color:var(--grey-text)}

  .team-photo{position:absolute;left:535px;top:708px;width:325px;height:195px;
    background:linear-gradient(135deg,#eef3f7 0%,#c9d6e0 55%,#2b3a4c 100%)}
  .contact{position:absolute;left:535px;top:918px;width:325px}
  .contact-lead{font-size:19px;line-height:1.25;color:var(--grey-text)}
  .contact-hours{font-weight:700;font-size:19px;line-height:1.25;color:var(--blue)}
  .contact-invite{font-size:19px;line-height:1.25;color:var(--grey-text)}
  .contact-bar{margin-top:10px;background:var(--navy);color:var(--white);font-family:'Oswald',Impact,sans-serif;font-weight:500;font-size:20px;padding:3px 14px;text-align:right}
  .phone{display:flex;align-items:center;gap:10px;margin-top:8px;font-weight:700;font-size:21px;color:var(--navy)}

  .footer-strip{position:absolute;left:0;top:1142px;width:900px;height:8px;background:var(--blue)}
  .footer{position:absolute;left:0;top:1150px;width:900px;height:50px;background:var(--navy-deep);display:flex;justify-content:center;align-items:center;gap:60px;color:var(--white);font-size:14px}
  .footer-item{display:flex;align-items:center;gap:8px}
</style>
</head>
<body>
<div class="flyer">

  <div class="hero-photo" role="img" aria-label="Container ship at a port at sunset with cranes and a cargo airplane flying overhead"></div>
  <svg class="hero-overlay" width="900" height="390" viewBox="0 0 900 390" aria-hidden="true">
    <polygon points="0,0 240,0 0,150" fill="#0d2a4d" opacity=".9"/>
    <polygon points="900,270 900,390 660,390" fill="#0d2a4d" opacity=".6"/>
  </svg>

  <header class="header">
    <svg class="header-accent" width="400" height="150" viewBox="0 0 400 150" aria-hidden="true">
      <polygon points="110,0 400,0 400,150 290,150" fill="#1f8fd6"/>
      <polygon points="220,0 400,0 400,90" fill="#0d2a4d"/>
      <polygon points="50,0 130,0 320,150 260,150" fill="#49b4ef" opacity=".7"/>
    </svg>
    <div class="brand">
      <div class="brand-dot"></div>
      <div class="brand-name">HALVORN FREIGHT INC</div>
    </div>
  </header>

  <section class="headline">
    <h1>YOUR SOLUTION</h1>
    <p>TO ALL YOUR <strong>SHIPPING NEEDS!</strong></p>
  </section>

  <section class="services ocean">
    <h2 class="services-title">Our most common<span>ocean services</span></h2>
    <ul class="services-list">
      <li>FCL (Full Container Load) import and export</li>
      <li>LCL (Less than Container Load) import and export</li>
      <li>General cargo to Dangerous loads</li>
      <li>Personal effects, residential pick up &amp; delivery</li>
      <li>Marketnest door importing from China or export stock to US</li>
    </ul>
  </section>

  <section class="services other">
    <h2 class="services-title">Other services</h2>
    <ul class="services-list">
      <li>Air/Ocean Freight Forwarding</li>
      <li>Inland Transportation for full truckloads and less than truckloads</li>
      <li>Customs Brokerage with our own AMS system</li>
      <li>Automotive shipping</li>
      <li>Personal effects shipping</li>
      <li>Courier services</li>
      <li>Over the road cross border shipping for Canada and Mexico</li>
    </ul>
  </section>

  <div class="team-photo" role="img" aria-label="Smiling customer service team in business attire"></div>

  <section class="contact">
    <p class="contact-lead">Our friendly staff is available</p>
    <p class="contact-hours">24 hours a day, 7 days a week</p>
    <p class="contact-invite">feel free to contact us:</p>
    <div class="contact-bar">CONTACT US</div>
    <div class="phone">
      <svg width="20" height="20" viewBox="0 0 24 24" aria-hidden="true"><path fill="#1f8fd6" d="M6.6 10.8a15.1 15.1 0 0 0 6.6 6.6l2.2-2.2c.3-.3.7-.4 1-.2 1.1.4 2.3.6 3.6.6.6 0 1 .4 1 1V20c0 .6-.4 1-1 1C10.6 21 3 13.4 3 4c0-.6.4-1 1-1h3.5c.6 0 1 .4 1 1 0 1.3.2 2.5.6 3.6.1.3 0 .7-.2 1z"/></svg>
      1-555-014-7720
    </div>
    <div class="phone">
      <svg width="20" height="20" viewBox="0 0 24 24" aria-hidden="true"><path fill="#1f8fd6" d="M6.6 10.8a15.1 15.1 0 0 0 6.6 6.6l2.2-2.2c.3-.3.7-.4 1-.2 1.1.4 2.3.6 3.6.6.6 0 1 .4 1 1V20c0 .6-.4 1-1 1C10.6 21 3 13.4 3 4c0-.6.4-1 1-1h3.5c.6 0 1 .4 1 1 0 1.3.2 2.5.6 3.6.1.3 0 .7-.2 1z"/></svg>
      1-555-014-7721
    </div>
  </section>

  <div class="footer-strip"></div>
  <footer class="footer">
    <span class="footer-item">
      <svg width="16" height="12" viewBox="0 0 16 12" aria-hidden="true"><rect x=".5" y=".5" width="15" height="11" fill="none" stroke="#49b4ef"/><path d="M.5 .5 8 7l7.5-6.5" fill="none" stroke="#49b4ef"/></svg>
      info@halvornfreight.com
    </span>
    <span class="footer-item">
      <svg width="14" height="14" viewBox="0 0 14 14" aria-hidden="true"><circle cx="7" cy="7" r="6.3" fill="none" stroke="#49b4ef"/><path d="M.7 7h12.6M7 .7c-3 3.5-3 9 0 12.6M7 .7c3 3.5 3 9 0 12.6" fill="none" stroke="#49b4ef"/></svg>
      www.halvornfreight.com
    </span>
  </footer>

</div>
</body>
</html>
```